Plumbing & Heating bussiness card design

i do all plumbing and heating work and need a catchy design. keep it simple but eye catching nothing gimicky
i do 24hr call outs
landlord safety checks
all aspects of plumbing and heating
boiler breakdowns
flue sure reg number 648197
i have put up my old card. not to bothered about the front but i have put up the back for the details. mobile number and office are the same and the email has changed to dantapfixer@brevomail.net

Industry/Entity Type

Safety

Contact Information for Business Card

i do 24hr call outs
landlord safety checks
boiler breakdowns

Requirements
Must have
• i do 24hr call outs
• landlord safety checks
• all aspects of plumbing and heating
• boiler breakdowns
• flue sure reg number 648197

```html
<!DOCTYPE html>
<html lang="en">
<head>
<meta charset="utf-8">
<title>B Hollins Plumbing &amp; Heating – Business Card</title>
<link href="https://fonts.googleapis.com/css2?family=Open+Sans:wght@400;600&family=Tinos:wght@400&display=swap" rel="stylesheet">
<style>
  :root {
    --backdrop: #e9e6e1;
    --card-white: #f4f4f4;
    --brand-red: #b0102a;
    --brand-blue: #4a7fbf;
    --ink-dark: #4a4a4c;
    --text-light: #f6e9ea;
    --text-soft: #e4ecf6;
  }
  * { margin: 0; padding: 0; box-sizing: border-box; }
  html, body { width: 1200px; height: 870px; overflow: hidden; }
  body {
    background: var(--backdrop);
    display: flex; align-items: center; justify-content: center;
    font-family: "Open Sans", Arial, sans-serif;
  }
  .business-card {
    position: relative;
    width: 470px; height: 720px;
    background: var(--card-white);
    box-shadow: 0 10px 30px rgba(0,0,0,.18);
    overflow: hidden;
  }
  .card-shapes { position: absolute; inset: 0; }
  .brand {
    position: absolute; top: 96px; left: 0; right: 0;
    display: flex; flex-direction: column; align-items: center; gap: 14px;
  }
  .brand-dot { width: 54px; height: 54px; border-radius: 50%; background: var(--brand-red); }
  .brand-name {
    font-weight: 600; color: var(--ink-dark);
    font-size: 36px; line-height: 1.12; text-align: center; letter-spacing: .5px;
  }
  .contact-block {
    position: absolute; top: 392px; left: 0; right: 0;
    text-align: center; color: var(--text-light);
  }
  .person-name { font-family: "Tinos", "Times New Roman", serif; font-size: 40px; line-height: 1; }
  .person-title { font-size: 19px; margin-top: 4px; }
  .contact-list { list-style: none; margin-top: 18px; font-size: 20px; line-height: 1.42; }
  .services {
    position: absolute; bottom: 16px; left: 0; right: 0;
    text-align: center; color: var(--text-soft); font-size: 16px; line-height: 1.36;
  }
</style>
</head>
<body>
  <article class="business-card">
    <svg class="card-shapes" width="470" height="720" viewBox="0 0 470 720">
      <path d="M0 370 C140 345 300 300 470 300 L470 720 L0 720 Z" fill="var(--brand-blue)"/>
      <path d="M0 378 C140 353 300 308 470 308 L470 720 L0 720 Z" fill="var(--brand-red)"/>
      <path d="M0 604 C160 598 320 586 470 580 L470 720 L0 720 Z" fill="var(--brand-blue)"/>
    </svg>

    <header class="brand">
      <span class="brand-dot" aria-hidden="true"></span>
      <h1 class="brand-name">B HOLLINS<br>PLUMBING &amp; HEATING</h1>
    </header>

    <section class="contact-block">
      <h2 class="person-name">Marcus D.Whitley</h2>
      <p class="person-title">President &amp; CEO</p>
      <ul class="contact-list">
        <li>555-013-2947</li>
        <li>dantapfixer@brevomail.net</li>
        <li>www.hollinsplumbing.net</li>
      </ul>
    </section>

    <p class="services">i do 24hr call outs,landlord safety checks,<br>all aspects of plumbing and heating,<br>boiler breakdowns<br>flue sure reg number 648197</p>
  </article>
</body>
</html>
```